Harbor of Bright Morning Paths, LLC needs business stationary designed using our logo.

Harbor of Bright Morning Paths is a new life coaching business. We have a logo design . We need a design for stationary for branding a new PathCrafter Life Coach business. We help people transform their lives by exploring, designing and taking action steps for the life they love in the areas of health and wellness, relationships, vocation, and time and money freedom. We like bright happy colors that present growth and transformation and also compliments the blue logo design.

Hello Designers, Thank you for accepting my design request. I wanted to be sure I put all the information for the business stationary design. If this is already in the order please disregard. Information to incorporate into stationary design Logo: incorporate blues and complimentary color Company name: Harbor of Bright Morning Paths, LLC Tagline: Transformational Life Coaching "If you can think it, you can do it You CAN live a life you LOVE! Website: www.norasaltwell.PathCrafterGuide.com Email: norasaltwell@PathCrafterGuide.com P.O. Box 5293 Edcouch, TX 78538 555-017-392 Nora T. Saltwell, Certified PathCrafter* Coach Positive, upbeat, professional design Thank you.

Industry/Entity Type

Life Coaching

Font styles to use
Decorative

Colors
0355a3

Requirements
Must have
• Information to incorporate into stationary design
• Logo: incorporate blues and complimentary color
• Company name: Harbor of Bright Morning Paths, LLC
• Tagline: Transformational Life Coaching
• "If you can think it, you can do it You CAN live a life you LOVE!
• Website: www.norasaltwell.PathCrafterGuide.com
• Email: norasaltwell@PathCrafterGuide.com
• P.O. Box 5293 Edcouch, TX 78538 555-017-392
• Nora T. Saltwell, Certified PathCrafter* Coach
• Positive, upbeat, professional design
Nice to have
• Watermark
Should not have
• No negativity or negative vibes
• Nothing derogatory
• No clashing colors

```html
<!DOCTYPE html>
<html lang="en">
<head>
<meta charset="utf-8">
<title>Harbor of Bright Morning Paths, LLC — Stationery</title>
<link href="https://fonts.googleapis.com/css2?family=Montserrat:wght@300;400;600;800&display=swap" rel="stylesheet">
<style>
  :root {
    --bg: #d0d0d0;
    --purple: #652a90;
    --indigo: #3d1cbe;
    --blue: #2a10e0;
    --paper: #ffffff;
    --ink: #444444;
    --muted: #666666;
    --mist: #f6f6f8;
  }
  * { margin: 0; padding: 0; box-sizing: border-box; }
  html, body { width: 1200px; height: 1041px; overflow: hidden; background: var(--bg); }
  body { position: relative; font-family: "Montserrat", sans-serif; }

  .piece { position: absolute; overflow: hidden; box-shadow: 0 1px 3px rgba(0,0,0,.25); }
  .brand-fill { background: linear-gradient(135deg, var(--purple) 0%, var(--indigo) 100%); }
  .paper { background: var(--paper); }

  .mark { position: absolute; border-radius: 50%; }
  .mark--brand { background: linear-gradient(135deg, var(--purple), var(--indigo)); }
  .mark--white { background: var(--paper); }
  .mark--faint { background: var(--mist); }

  .brand-name { position: absolute; color: var(--blue); font-weight: 800; line-height: 1.1; }
  .tagline { display: block; color: var(--muted); font-weight: 400; }

  /* Plain footer band */
  .footer-band { position: absolute; left: 0; bottom: 0; width: 100%; }
  .footer-band__line { height: 2px; background: var(--blue); }
  .footer-band__fill { background: linear-gradient(90deg, var(--purple), var(--indigo)); }

  /* Folder */
  .folder { left: 166px; top: 76px; width: 417px; height: 541px; border-radius: 3px; }
  .folder__spine { position: absolute; left: 0; top: 0; width: 29px; height: 100%; border-right: 2px solid rgba(0,0,0,.12); background: rgba(255,255,255,.03); }
  .folder .mark { left: 147px; top: 179px; width: 146px; height: 146px; }
  .folder__name { position: absolute; left: 0; width: 100%; top: 477px; text-align: center; color: var(--paper); font-weight: 800; font-size: 13.5px; }
  .folder__tag { position: absolute; left: 0; width: 100%; top: 495px; text-align: center; color: var(--paper); font-weight: 300; font-size: 10px; letter-spacing: .3px; }

  /* Letterhead */
  .letterhead { left: 615px; top: 95px; width: 403px; height: 522px; }
  .letterhead .mark--brand { left: 32px; top: 39px; width: 37px; height: 37px; }
  .letterhead .mark--faint { left: 67px; top: 166px; width: 262px; height: 262px; }
  .letterhead .brand-name { left: 76px; top: 42px; font-size: 9.5px; }
  .letterhead .tagline { font-size: 7px; margin-top: 2px; }
  .letterhead .footer-band__fill { height: 10px; }
  .contact { position: absolute; right: 28px; top: 38px; text-align: right; font-size: 4.6px; color: var(--ink); line-height: 1.55; }
  .contact__gap { height: 3px; }
  .contact__icon { display: inline-block; width: 4px; height: 4px; margin-left: 3px; border-radius: 50%; background: var(--blue); vertical-align: middle; }

  /* Envelope front */
  .envelope { left: 132px; top: 645px; width: 451px; height: 196px; }
  .envelope .mark--brand { left: 25px; top: 26px; width: 33px; height: 33px; }
  .envelope .mark--faint { left: 232px; top: 45px; width: 180px; height: 180px; }
  .envelope .brand-name { left: 63px; top: 32px; font-size: 8px; }
  .envelope .tagline { font-size: 6px; margin-top: 2px; }
  .envelope .footer-band__fill { height: 8px; }
  .envelope__address { position: absolute; left: 28px; top: 161px; font-size: 5px; color: var(--ink); line-height: 1.5; }

  /* Envelope back */
  .envelope-back { left: 615px; top: 645px; width: 451px; height: 196px; }
  .envelope-back__flap { position: absolute; left: 0; top: 0; width: 100%; height: 66px; }
  .envelope-back .mark { left: 214px; top: 21px; width: 25px; height: 25px; }

  /* Business cards */
  .card { top: 872px; width: 165px; height: 91px; border-radius: 3px; }
  .card--front { left: 418px; }
  .card--front .mark { left: 30px; top: 24px; width: 24px; height: 24px; }
  .card--front .footer-band__fill { height: 3px; }
  .card__name { position: absolute; left: 6px; width: 72px; top: 53px; text-align: center; color: var(--blue); font-weight: 800; font-size: 3.6px; line-height: 1.3; }
  .card__details { position: absolute; left: 83px; top: 26px; font-size: 3.3px; color: var(--ink); line-height: 1.6; }
  .card__person { color: var(--blue); font-weight: 600; font-size: 5px; line-height: 1.2; }
  .card__role { font-size: 3.2px; margin-bottom: 3px; }
  .card--back { left: 616px; }
  .card--back .mark { left: 63px; top: 19px; width: 38px; height: 38px; }
  .card--back .card__name { left: 0; width: 100%; top: 70px; color: var(--paper); font-size: 5.6px; }
  .card--back .card__tag { position: absolute; left: 0; width: 100%; top: 78px; text-align: center; color: var(--paper); font-size: 3.8px; font-weight: 300; }
</style>
</head>
<body>

<section class="piece folder brand-fill" aria-label="Presentation folder">
  <div class="folder__spine"></div>
  <div class="mark mark--white"></div>
  <p class="folder__name">Harbor of Bright Morning Paths, LLC</p>
  <p class="folder__tag">Transformational Coaching</p>
</section>

<section class="piece letterhead paper" aria-label="Letterhead">
  <div class="mark mark--faint"></div>
  <div class="mark mark--brand"></div>
  <p class="brand-name">Harbor of Bright<br>Morning Paths, LLC<span class="tagline">Transformational Coaching</span></p>
  <div class="contact">
    <p>P.O. Box 5293</p>
    <p>Millbrook, TX 75910</p>
    <div class="contact__gap"></div>
    <p>555-017-392<span class="contact__icon"></span></p>
    <p>norasaltwell@PathCrafterGuide.com<span class="contact__icon"></span></p>
    <p>www.norasaltwell.PathCrafterGuide.com<span class="contact__icon"></span></p>
  </div>
  <div class="footer-band"><div class="footer-band__line"></div><div class="footer-band__fill"></div></div>
</section>

<section class="piece envelope paper" aria-label="Envelope front">
  <div class="mark mark--faint"></div>
  <div class="mark mark--brand"></div>
  <p class="brand-name">Harbor of Bright<br>Morning Paths, LLC<span class="tagline">Transformational Coaching</span></p>
  <p class="envelope__address">P.O. Box 5293<br>Millbrook, TX 75910</p>
  <div class="footer-band"><div class="footer-band__line"></div><div class="footer-band__fill"></div></div>
</section>

<section class="piece envelope-back paper" aria-label="Envelope back">
  <svg class="envelope-back__flap" viewBox="0 0 451 66" preserveAspectRatio="none">
    <defs>
      <linearGradient id="flap-fill" x1="0" x2="1">
        <stop offset="0" stop-color="#652a90"/><stop offset="1" stop-color="#3d1cbe"/>
      </linearGradient>
    </defs>
    <path d="M0 0 H451 L439 64 Q438 66 435 66 H20 Q16 66 15 63 Z" fill="url(#flap-fill)"/>
  </svg>
  <div class="mark mark--white"></div>
</section>

<section class="piece card card--front paper" aria-label="Business card front">
  <div class="mark mark--brand"></div>
  <p class="card__name">HARBOR OF BRIGHT<br>MORNING PATHS, LLC</p>
  <div class="card__details">
    <p class="card__person">Nora T. Saltwell</p>
    <p class="card__role">Certified PathCrafter</p>
    <p>555-017-392</p>
    <p>norasaltwell@PathCrafterGuide.com</p>
    <p>www.norasaltwell.PathCrafterGuide.com</p>
    <p>P.O. Box 5293, Millbrook, TX 75910</p>
  </div>
  <div class="footer-band"><div class="footer-band__line"></div><div class="footer-band__fill"></div></div>
</section>

<section class="piece card card--back brand-fill" aria-label="Business card back">
  <div class="mark mark--white"></div>
  <p class="card__name">Harbor of Bright Morning Paths, LLC</p>
  <p class="card__tag">Transformational Coaching</p>
</section>

</body>
</html>
```